Business cards

I would like a black background with the design I previously chose. I need 2 sets of cards. Mine will have Marisol Brandt, Broker/Owner, 307-555-0148 and marisol.harborpeak@mailvista.com
The second set will read, Dana Rutledge, Realtor 307-555-0172, dana.harborpeak@mailvista.com

Industry/Entity Type

Business

```html
<!DOCTYPE html>
<html lang="en">
<head>
<meta charset="utf-8">
<title>Business Cards – Marisol Brandt &amp; Dana Rutledge</title>
<link rel="stylesheet" href="https://fonts.googleapis.com/css2?family=Jost:wght@400;500;600&display=swap">
<style>
  :root {
    --page: #d9d6d1;
    --card-top: #262626;
    --card-bottom: #0e0e0e;
    --accent: #e3151b;
    --ink: #f4f4f4;
    --muted: #bdbdbd;
  }
  * { box-sizing: border-box; margin: 0; padding: 0; }
  html, body {
    width: 1200px; height: 900px; overflow: hidden;
    background: var(--page);
    font-family: "Jost", "Futura", sans-serif;
  }
  .sheet {
    width: 1200px; height: 900px;
    display: flex; flex-direction: column;
    align-items: center; justify-content: center; gap: 50px;
  }
  .card {
    position: relative;
    width: 700px; height: 400px;
    background: radial-gradient(ellipse at 50% 25%, var(--card-top), var(--card-bottom) 80%);
    box-shadow: 0 10px 24px rgba(0,0,0,.35);
    color: var(--ink);
  }
  .card__identity {
    position: absolute; top: 106px; left: 0; right: 0;
  }
  .identity__name-row {
    display: flex; align-items: center;
  }
  .identity__spacer { flex: 1; }
  .identity__rule {
    height: 2px; background: var(--accent);
  }
  .identity__rule--upper {
    flex: 1; margin-left: 22px; transform: translateY(6px);
  }
  .card__name {
    flex: none;
    font-weight: 600; font-size: 30px; letter-spacing: 4px;
    text-transform: uppercase; color: var(--accent);
    line-height: 1;
  }
  .identity__role-row {
    display: flex; align-items: flex-end; margin-top: 6px;
  }
  .identity__rule--lower {
    flex: 1.35; margin-right: 22px; margin-bottom: -22px;
  }
  .identity__role-row .identity__spacer { flex: 0.65; }
  .card__role {
    flex: none;
    font-weight: 400; font-size: 19px; letter-spacing: 1.5px;
    color: var(--muted); line-height: 1.1;
  }
  .card__contacts {
    position: absolute; top: 228px; left: 0; right: 0;
    display: flex; flex-direction: column; align-items: center; gap: 26px;
    font-weight: 500; font-size: 22px; letter-spacing: 2px;
  }
  .contact { display: flex; align-items: center; gap: 12px; }
  .contact__icon { width: 26px; height: 26px; flex: none; }
</style>
</head>
<body>
<main class="sheet">

  <section class="card" aria-label="Business card for Dana Rutledge">
    <div class="card__identity">
      <div class="identity__name-row">
        <span class="identity__spacer"></span>
        <h2 class="card__name">Dana Rutledge</h2>
        <span class="identity__rule identity__rule--upper"></span>
      </div>
      <div class="identity__role-row">
        <span class="identity__rule identity__rule--lower"></span>
        <span class="card__role">Realtor</span>
        <span class="identity__spacer"></span>
      </div>
    </div>
    <div class="card__contacts">
      <p class="contact">
        <svg class="contact__icon" viewBox="0 0 26 26" aria-hidden="true">
          <circle cx="13" cy="13" r="11.5" fill="none" stroke="var(--accent)" stroke-width="1.6"/>
          <rect x="9" y="6.5" width="8" height="13" rx="1.5" fill="none" stroke="var(--accent)" stroke-width="1.6"/>
          <line x1="11.5" y1="17" x2="14.5" y2="17" stroke="var(--accent)" stroke-width="1.2"/>
        </svg>
        <span>307-555-0172</span>
      </p>
      <p class="contact">
        <svg class="contact__icon" viewBox="0 0 26 26" aria-hidden="true">
          <circle cx="13" cy="13" r="11.5" fill="none" stroke="var(--accent)" stroke-width="1.6"/>
          <rect x="7" y="8.5" width="12" height="9" fill="var(--accent)"/>
          <polyline points="7,8.5 13,13.5 19,8.5" fill="none" stroke="#111" stroke-width="1.2"/>
        </svg>
        <span>dana.harborpeak@mailvista.com</span>
      </p>
    </div>
  </section>

  <section class="card" aria-label="Business card for Marisol Brandt">
    <div class="card__identity">
      <div class="identity__name-row">
        <span class="identity__spacer"></span>
        <h2 class="card__name">Marisol Brandt</h2>
        <span class="identity__rule identity__rule--upper"></span>
      </div>
      <div class="identity__role-row">
        <span class="identity__rule identity__rule--lower"></span>
        <span class="card__role">Broker/Owner</span>
        <span class="identity__spacer"></span>
      </div>
    </div>
    <div class="card__contacts">
      <p class="contact">
        <svg class="contact__icon" viewBox="0 0 26 26" aria-hidden="true">
          <circle cx="13" cy="13" r="11.5" fill="none" stroke="var(--accent)" stroke-width="1.6"/>
          <rect x="9" y="6.5" width="8" height="13" rx="1.5" fill="none" stroke="var(--accent)" stroke-width="1.6"/>
          <line x1="11.5" y1="17" x2="14.5" y2="17" stroke="var(--accent)" stroke-width="1.2"/>
        </svg>
        <span>307-555-0148</span>
      </p>
      <p class="contact">
        <svg class="contact__icon" viewBox="0 0 26 26" aria-hidden="true">
          <circle cx="13" cy="13" r="11.5" fill="none" stroke="var(--accent)" stroke-width="1.6"/>
          <rect x="7" y="8.5" width="12" height="9" fill="var(--accent)"/>
          <polyline points="7,8.5 13,13.5 19,8.5" fill="none" stroke="#111" stroke-width="1.2"/>
        </svg>
        <span>marisol.harborpeak@mailvista.com</span>
      </p>
    </div>
  </section>

</main>
</body>
</html>
```